Striking new Advert required for Commercial Real Estate Agency

We need a a NEW newspaper advertisement for the marketing of a large commercial property (a Backpackers lodge)

Dimensions are to be width of 101mm and height of 100mm (10cms)

Our key design statement for this advert is clean, modern and minimalist design, with accents of 'HOT PINK' colour to remove it from looking too boring, perhaps in the area of the contact icons. The heirachy of the advert is outlined in the attached ADVERTISEMENT TEXT FILE.

Our company name is THE MERIDAL COLLECTIVE, and we want our brand to appear professional yet classy in it's design style (sort of like an advertising or design agency)

We have two logo options below, one more square in its layout (which we prefer) and the other more rectangular, which may be better suited for the layout. We are not adverse to the logo being reversed (white text on black), along with other key element areas such as the main advert heading and the "FOR SALE" part, and think this would be a good option.
There are two photos attached to be included in the advert.

We have attached an example of an old advert that we did, which we DID NOT LIKE, and which was for a smaller width than the one we need (it is only 65% of the width of this one). WE have also atached a file showing layout of some of our competitors adverts, which we dont think are too good either.

We are really open for ideas, but have time pressures, so please come back with any questions as soon as you can, if needed.

Thank you
Updates

Thank you for the great and diverse designs. There are a few standout options, but one style that we prefer most.

Target Market(s)

We are wanting this newspaper advertisement to attract interest from real estat e developers, investors and motel/lodge owners, along with other high nett worth individuals

Industry/Entity Type

Real Estate

Font styles to use
Serif
Sans Serif

Colors
1b1b1b
a54499
474747
fbfbfb

Requirements
Must have
• Clean modern look, predominantly monochromatic or black and white, with the hot pink accent somewhere, as mentioned above.
• All the contents of the TEXT provided, perhaps with additional space to add a little more if needed, Please advise if you think we dont have enough space for all of the TEXT
Should not have
• Script like fonts
• Cartoonish characters
• a 'cheap' look

```html
<!DOCTYPE html>
<html lang="en">
<head>
<meta charset="utf-8">
<title>Mount Victoria Land Grab – For Sale</title>
<link href="https://fonts.googleapis.com/css2?family=Montserrat:wght@400;500;600&family=Roboto+Condensed:wght@400;700&display=swap" rel="stylesheet">
<style>
  :root {
    --pink: #b0197f;
    --ink: #1b1b1b;
    --grey: #474747;
    --paper: #ffffff;
    --stage: #e4e4e4;
    --bar: #231f20;
  }
  * { margin: 0; padding: 0; box-sizing: border-box; }
  html, body { width: 1200px; height: 1000px; overflow: hidden; }
  body { background: var(--stage); position: relative; font-family: "Roboto Condensed", sans-serif; color: var(--ink); }

  .advert { position: absolute; left: 161px; top: 65px; width: 879px; height: 870px; background: var(--paper); }

  .sale-band { position: absolute; left: 0; top: 0; width: 119px; height: 472px; background: var(--pink); }
  .sale-band__text {
    position: absolute; left: 59px; top: 236px;
    transform: translate(-50%, -50%) rotate(-90deg);
    white-space: nowrap; color: var(--paper);
    font-family: "Montserrat", sans-serif; font-weight: 500; font-size: 78px; letter-spacing: 4px;
  }

  .hero-photo {
    position: absolute; left: 119px; top: 0; width: 760px; height: 472px;
    background: linear-gradient(180deg, #5b8fd6 0%, #8fb4e6 30%, #e8e6df 45%, #d9d7cf 65%, #5f7a3c 85%, #3f5a2a 100%);
  }

  .title-bar { position: absolute; left: 0; top: 472px; width: 879px; height: 63px; background: var(--bar); color: var(--paper); text-align: right; padding: 9px 35px 0 0; font-family: "Montserrat", sans-serif; }
  .title-bar__heading { font-size: 19px; font-weight: 500; letter-spacing: 0.5px; line-height: 23px; }
  .title-bar__address { font-size: 16px; font-weight: 500; line-height: 22px; }

  .details { position: absolute; left: 27px; top: 539px; width: 800px; font-size: 21px; line-height: 27px; color: var(--ink); }
  .details__list { list-style: none; }
  .details__list li { position: relative; padding-left: 17px; }
  .details__list li::before { content: ""; position: absolute; left: 0; top: 9px; width: 9px; height: 9px; background: var(--pink); }

  .tender { position: absolute; left: 27px; top: 748px; font-size: 20px; font-weight: 700; color: var(--pink); }
  .contact { position: absolute; left: 27px; top: 782px; font-size: 18px; font-weight: 700; line-height: 27px; color: var(--ink); }
  .contact__phones { display: flex; align-items: center; gap: 6px; font-size: 19px; }
  .contact__icon { width: 17px; height: 17px; }
  .contact__phones .gap { width: 12px; }
  .contact__web em { font-style: normal; color: var(--pink); }

  .brand { position: absolute; left: 590px; top: 770px; display: flex; align-items: center; gap: 22px; }
  .brand__square { width: 80px; height: 80px; background: var(--ink); }
  .brand__name { font-family: "Montserrat", sans-serif; font-weight: 400; font-size: 21px; line-height: 25px; letter-spacing: 1.5px; color: var(--ink); }
</style>
</head>
<body>
  <article class="advert">
    <div class="sale-band"><span class="sale-band__text">FOR SALE</span></div>
    <div class="hero-photo" role="img" aria-label="Photo of a large white two-storey weatherboard backpackers lodge with balconies and a bay window, beside a narrow lane with green shrubs under a blue sky"></div>

    <header class="title-bar">
      <h1 class="title-bar__heading">MOUNT VICTORIA LAND GRAB</h1>
      <p class="title-bar__address">Harlow’s Lodge, 42 Calder Street, Mount Victoria</p>
    </header>

    <section class="details">
      <p>This Old Beauty has served many, and is now ripe for development.</p>
      <p>One of Mt Vic’s largest land areas, now offered with vacant possession, with key details being:</p>
      <ul class="details__list">
        <li>Large Land area of 2076m² with elevated sunny position and great outlook + access from Wexford Street</li>
        <li>Existing Backpackers Lodge of 970m² providing multiple rooms with amenity areas</li>
        <li>Four adjacent sites also available, taking total land area to 4452m², an unprecedented Land Offering in this popular city fringe location</li>
      </ul>
    </section>

    <p class="tender">Now Selling by Closed Tender</p>

    <section class="contact">
      <p>Contact the Sole Agent : Daniel Moreau</p>
      <p class="contact__phones">
        <svg class="contact__icon" viewBox="0 0 24 24" aria-hidden="true"><path fill="#b0197f" d="M6.6 10.8a15.1 15.1 0 0 0 6.6 6.6l2.2-2.2c.3-.3.7-.4 1-.2 1.1.4 2.3.6 3.6.6.6 0 1 .4 1 1V20c0 .6-.4 1-1 1A17 17 0 0 1 3 4c0-.6.4-1 1-1h3.5c.6 0 1 .4 1 1 0 1.3.2 2.5.6 3.6.1.3 0 .7-.2 1z"/></svg>
        <span>(04) 555 0142</span>
        <span class="gap"></span>
        <svg class="contact__icon" viewBox="0 0 24 24" aria-hidden="true"><rect x="6" y="2" width="12" height="20" rx="2" fill="none" stroke="#b0197f" stroke-width="2"/><circle cx="12" cy="18.5" r="1.2" fill="#b0197f"/></svg>
        <span>(021) 555 0187</span>
      </p>
      <p class="contact__web">daniel@meridalcollective.co.nz &nbsp;|&nbsp; www.<em>meridalcollective</em>.co.nz</p>
    </section>

    <div class="brand">
      <span class="brand__square" aria-hidden="true"></span>
      <p class="brand__name">THE<br>MERIDAL<br>COLLECTIVE</p>
    </div>
  </article>
</body>
</html>
```